Business card

I am a contemporary jeweller from Melbourne, Australia. I am after a great crisp and sophisticated business card. My ideas are very specific and I have a few files attached which are pretty much what I am after but i believe it needs refining and also the quality is too poor for printing, so it would need to be cleaned up a lot.

On one side I would like a logo with my initials (similar to the files I have attached - but a little more aesthetically pleasing) to somewhat match the font that I have attached. I would like a M and a T in lower case to be "hugging" each other - with the t inside the m. I want it to look like letters but also be attractive. I would also like it to look round and neat. The logo should look like a jeweller's hallmark stamp (as this logo will also be used as my Hallmark, and therefore needs to be crisp, sharp and simple so that it reads well on a small scale (2mm) and also on print media).

The business card layout should be on one side - my logo placed somewhere not very large and that is all.

on the other side of the card i would like my contact details without the logo anywhere.

I have attached what I would like the back of my card to look like, and also the font which I like which i found on www.glyphorama.com called "The Skinny" and "The Skinny Bold". I love this font, but it loses quality when the size is reduced. I am unsure of what the font should be for my contact details so I am open to suggestions. I do feel that it should be different to The Skinny font and probably lower case.

I know that the following is not something that is in your control but it may give you an idea of what I like:
I will be having the business cards printed on quite thick and textured card and possibly embossed. It will be black font on white or off white paper.
Also, please find attached images of a business card I really like.

Thanks,
If you have any questions please contact me.

Industry/Entity Type

Business

Requirements
Nice to have
• MIRELA TUVIN (The Skinny Font or similar)
• Jeweller - designer
• fine contemporary jewellery
• +61 452 918 034
• info@mirelatuvin.com
• www.mirelatuvin.com

```html
<!DOCTYPE html>
<html lang="en">
<head>
<meta charset="utf-8">
<title>Mirela Tuvin — Business Card</title>
<link rel="stylesheet" href="https://fonts.googleapis.com/css2?family=Amatic+SC:wght@400&family=Ubuntu:wght@400&display=swap">
<style>
  :root {
    --backdrop: #e6e3df;
    --card: #ffffff;
    --ink: #1c1c1c;
    --ink-soft: #3a3a3a;
    --shadow: rgba(0, 0, 0, 0.18);
  }
  * { box-sizing: border-box; margin: 0; padding: 0; }
  html, body {
    width: 1200px;
    height: 1000px;
    overflow: hidden;
    background: var(--backdrop);
  }
  .canvas {
    position: relative;
    width: 1200px;
    height: 1000px;
  }
  .card {
    position: absolute;
    left: 260px;
    width: 680px;
    height: 390px;
    background: var(--card);
    box-shadow: 0 6px 18px var(--shadow);
    color: var(--ink);
  }
  .card--front { top: 80px; }
  .card--back { top: 530px; }

  .front-mark {
    position: absolute;
    inset: 0;
    display: flex;
    align-items: center;
    justify-content: center;
    gap: 18px;
  }
  .front-mark__dot {
    width: 14px;
    height: 14px;
    border-radius: 50%;
    background: var(--ink);
  }
  .front-mark__name {
    font-family: "Amatic SC", sans-serif;
    font-size: 56px;
    letter-spacing: 6px;
    color: var(--ink);
  }

  .identity {
    position: absolute;
    top: 70px;
    left: 0;
    right: 0;
    text-align: center;
  }
  .identity__name {
    font-family: "Amatic SC", sans-serif;
    font-weight: 400;
    font-size: 54px;
    letter-spacing: 7px;
    line-height: 1;
    color: var(--ink-soft);
  }
  .identity__role {
    margin-top: 14px;
    font-family: "Amatic SC", sans-serif;
    font-size: 20px;
    letter-spacing: 4px;
    color: var(--ink-soft);
  }

  .contact {
    position: absolute;
    top: 232px;
    left: 0;
    right: 0;
    list-style: none;
    text-align: center;
    font-family: "Ubuntu", sans-serif;
    font-size: 18px;
    letter-spacing: 1.5px;
    line-height: 1.55;
    color: var(--ink);
  }
</style>
</head>
<body>
  <main class="canvas">
    <section class="card card--front" aria-label="Card front">
      <div class="front-mark">
        <span class="front-mark__dot"></span>
        <span class="front-mark__name">MIRELA TUVIN</span>
      </div>
    </section>

    <section class="card card--back" aria-label="Card back">
      <header class="identity">
        <h1 class="identity__name">MIRELA TUVIN</h1>
        <p class="identity__role">DESIGNER . JEWELLER</p>
      </header>
      <ul class="contact">
        <li class="contact__web">www.mirelatuvin.com</li>
        <li class="contact__email">info@mirelatuvin.com</li>
        <li class="contact__phone">+61 452 918 034</li>
      </ul>
    </section>
  </main>
</body>
</html>
```